Business card for my new company (Accounting firm)

I need a business card for my new business Corvane Advisory and Ledger SA. Our services are accounting, tax, audit and financial management. Our customers are small companies, start-ups and new companies. The final design has to show financial security, trust and growth. Please find our logo attached to the business card. Text for the business card: Corvane Advisory and Ledger SA Tomas da Varela Director and Founder Certified Accountant Tel. 022 418 27 35 tv@corvaneconseil.ch www.corvaneconseil.ch Rue des Vergers-Bleus 14 1201 Geneva
Target Market(s)
Our customers are small companies, start-ups and new companies.
Industry/Entity Type
Finance And Accounting
Contact Information for Business Card
Corvane Conseil et Registre SA
Tomas da Varela
Directeur et Fondateur
Expert-comptable diplômé
Tél. 022 418 27 35
tv@corvaneconseil.ch
www.corvaneconseil.ch
Rue des Vergers-Bleus 14
1201 Genève

```html
<!DOCTYPE html>
<html lang="fr">
<head>
<meta charset="utf-8">
<title>Corvane Conseil et Registre SA – Carte de visite</title>
<link rel="stylesheet" href="https://fonts.googleapis.com/css2?family=Montserrat:wght@400;500;700&display=swap">
<style>
  :root {
    --backdrop: #2e2e2e;
    --card-white: #ffffff;
    --ink: #3a3a3a;
    --ink-soft: #555555;
    --brand-blue: #1d7fc4;
    --brand-deep: #1a5f95;
    --brand-light: #28b0e2;
    --rule: #4a4a4a;
  }
  * { box-sizing: border-box; margin: 0; padding: 0; }
  html, body {
    width: 1200px; height: 900px; overflow: hidden;
    background: var(--backdrop);
    font-family: "Montserrat", sans-serif;
  }
  .sheet {
    width: 1200px; height: 900px;
    display: flex; flex-direction: column; align-items: center; justify-content: center;
    gap: 40px;
  }
  .card {
    width: 700px; height: 400px;
    position: relative;
    box-shadow: 0 12px 30px rgba(0,0,0,.45);
  }

  /* Front */
  .card-front { background: var(--card-white); color: var(--ink); }
  .holder { position: absolute; left: 44px; top: 46px; }
  .holder-name {
    font-size: 25px; font-weight: 700; color: var(--brand-blue);
    margin-bottom: 6px;
  }
  .holder-role { font-size: 15px; font-weight: 400; line-height: 1.4; color: var(--ink-soft); }
  .contact-list { list-style: none; margin-top: 12px; }
  .contact-list li {
    display: flex; align-items: center; gap: 10px;
    font-size: 15px; line-height: 1.55; color: var(--ink);
  }
  .contact-list svg { width: 14px; height: 14px; flex: none; fill: var(--brand-deep); }
  .divider {
    position: absolute; left: 300px; right: 40px; top: 176px;
    border-top: 1.5px solid var(--rule);
  }
  .front-mark {
    position: absolute; right: 52px; top: 58px;
    display: flex; align-items: center; gap: 10px;
  }
  .front-mark .square { width: 16px; height: 16px; background: var(--brand-blue); }
  .front-mark .wordmark {
    font-size: 34px; font-weight: 700; letter-spacing: 2px; color: var(--brand-deep);
  }
  .office {
    position: absolute; right: 44px; bottom: 48px;
    text-align: right; font-size: 17px; line-height: 1.45; color: var(--ink);
  }

  /* Back */
  .card-back {
    background: linear-gradient(135deg, var(--brand-deep) 0%, #1e88cc 55%, var(--brand-light) 100%);
    display: flex; align-items: center; justify-content: center; gap: 16px;
  }
  .card-back .square { width: 22px; height: 22px; background: #ffffff; }
  .card-back .wordmark {
    font-size: 52px; font-weight: 700; letter-spacing: 4px; color: #ffffff;
  }
</style>
</head>
<body>
<main class="sheet">
  <section class="card card-front" aria-label="Recto de la carte">
    <div class="holder">
      <h1 class="holder-name">Tomas da Varela</h1>
      <p class="holder-role">Directeur et Fondateur</p>
      <p class="holder-role">Expert-comptable diplômé</p>
      <ul class="contact-list">
        <li>
          <svg viewBox="0 0 24 24" aria-hidden="true"><path d="M6.6 10.8c1.4 2.8 3.8 5.1 6.6 6.6l2.2-2.2c.3-.3.7-.4 1-.2 1.1.4 2.3.6 3.6.6.6 0 1 .4 1 1V20c0 .6-.4 1-1 1C10.6 21 3 13.4 3 4c0-.6.4-1 1-1h3.5c.6 0 1 .4 1 1 0 1.3.2 2.5.6 3.6.1.3 0 .7-.2 1l-2.3 2.2z"/></svg>
          022 418 27 35
        </li>
        <li>
          <svg viewBox="0 0 24 24" aria-hidden="true"><path d="M2 5h20v14H2z M2 5l10 8 10-8" /><path d="M2 5l10 8 10-8v2l-10 8L2 7z" fill="#fff"/></svg>
          tv@corvaneconseil.ch
        </li>
        <li>
          <svg viewBox="0 0 24 24" aria-hidden="true"><path d="M12 2a10 10 0 1 0 0 20 10 10 0 0 0 0-20zm6.9 6h-3a15 15 0 0 0-1.3-3.9A8 8 0 0 1 18.9 8zM12 4c.8 1.2 1.5 2.5 1.9 4h-3.8c.4-1.5 1.1-2.8 1.9-4zM4.3 14a8 8 0 0 1 0-4h3.4a16 16 0 0 0 0 4H4.3zm.8 2h3a15 15 0 0 0 1.3 3.9A8 8 0 0 1 5.1 16zm3-8h-3a8 8 0 0 1 4.3-3.9C8.8 5.3 8.4 6.6 8.1 8zM12 20c-.8-1.2-1.5-2.5-1.9-4h3.8c-.4 1.5-1.1 2.8-1.9 4zm2.3-6H9.7a14 14 0 0 1 0-4h4.6a14 14 0 0 1 0 4zm.3 5.9c.6-1.2 1-2.5 1.3-3.9h3a8 8 0 0 1-4.3 3.9zm1.7-5.9a16 16 0 0 0 0-4h3.4a8 8 0 0 1 0 4h-3.4z"/></svg>
          www.corvaneconseil.ch
        </li>
      </ul>
    </div>
    <div class="divider" aria-hidden="true"></div>
    <div class="front-mark">
      <span class="square" aria-hidden="true"></span>
      <span class="wordmark">CORVANE</span>
    </div>
    <address class="office" style="font-style:normal">
      Corvane Conseil et Registre SA<br>
      Rue des Vergers-Bleus 14<br>
      1201 Genève
    </address>
  </section>

  <section class="card card-back" aria-label="Verso de la carte">
    <span class="square" aria-hidden="true"></span>
    <span class="wordmark">CORVANE</span>
  </section>
</main>
</body>
</html>
```